Solar panel installation company needs a flyer.

Need a double sided flyer (not sure what size at this stage) to attract new customers and engage them with our company. We supply and install solar panels for residential homes and want residents to see the sense in installing solar.
Ideally we need on the front page:
A photo of us installing solar panels so the customer can see the face of our business and who they are dealing with.
A question: "What will your electricity bill look like in 5 years time?"
An answer to the above question: "Install solar power today and start saving!" (with a picture of solar panels on roof and money underneath - see attached)
A section that says: "3 reasons to install solar..."
1 - "The sun provides ample amounts of free, clean energy every day."
2 - "The government provides generous incentives saving you thousands of $$."
3 - "Advanced technology allows you to store your energy and use it a night."
A call to action such as: "Call us now for a free quote." (Phone 0482 917 605).
Back page we need:
A simple table showing a price guide with original cost crossed out and discounted cost highlighted. And a section with more information under the table.
A section about our company with a picture of us.
A customer testimonial.
A footer section with more information such as business number, license numbers, website and terms of the price guide.
We want you to come up with creative, eye catching and easy to read ways to display the above information with enough white space so it doesn't seem too busy. We are open to other suggestions, colour scheme and amount of information that should be placed on the flyer.
We also need to display our website on both sides (www.tarnbrookservices.com.au)
Please find attached photos, logos and content for you to use in the best way possible.
If you feel images are not of quality we can arrange professional images to be taken and uploaded.
Home owners aged 30+
It Company

```html
<!DOCTYPE html>
<html lang="en">
<head>
<meta charset="utf-8">
<title>Tarnbrook Services – Solar Flyer</title>
<link rel="stylesheet" href="https://fonts.googleapis.com/css2?family=Oswald:wght@500;700&family=Open+Sans:wght@400;600;700&display=swap">
<style>
  :root {
    --orange: #f47b20;
    --orange-deep: #e2661a;
    --ink: #141414;
    --white: #ffffff;
    --sky: #7fb6e6;
    --panel: #2a4f86;
    --grey: #8a8f96;
  }
  * { box-sizing: border-box; margin: 0; padding: 0; }
  html, body { width: 900px; height: 1200px; overflow: hidden; background: var(--white); }
  .flyer { position: relative; width: 900px; height: 1200px; overflow: hidden; background: var(--white); font-family: "Open Sans", Arial, sans-serif; }

  .shapes { position: absolute; inset: 0; }

  .brand { position: absolute; left: 70px; top: 62px; display: flex; align-items: center; gap: 14px; }
  .brand-mark { width: 62px; height: 62px; background: var(--orange); flex: none; }
  .brand-name { font-family: "Oswald", Arial, sans-serif; font-weight: 700; font-size: 30px; line-height: 1.05; color: var(--orange); letter-spacing: 1px; text-transform: uppercase; }

  .headline { position: absolute; left: 60px; top: 215px; width: 330px; font-family: "Oswald", Arial, sans-serif; font-weight: 700; text-transform: uppercase; font-size: 46px; line-height: 1.12; color: var(--orange); }
  .headline .dark { color: var(--ink); font-size: 40px; }
  .headline .last { font-size: 40px; white-space: nowrap; }

  .portrait { position: absolute; width: 196px; height: 196px; border-radius: 50%; border: 7px solid var(--white); box-shadow: 0 0 0 4px var(--orange); }
  .portrait-switchboard { left: 150px; top: 560px; background: radial-gradient(circle at 45% 40%, #6d7680, #2c3238 70%); }
  .portrait-van { left: 150px; top: 860px; background: radial-gradient(circle at 50% 40%, #d9dde2, #3c4c63 75%); }

  .reasons { position: absolute; left: 440px; top: 690px; width: 430px; color: var(--white); text-align: right; }
  .reasons-title { font-family: "Oswald", Arial, sans-serif; font-weight: 700; text-transform: uppercase; line-height: 1.05; }
  .reasons-title .big { display: block; font-size: 50px; }
  .reasons-title .sub { display: block; font-size: 36px; }
  .reason-list { list-style: none; margin-top: 26px; }
  .reason { position: relative; font-size: 19px; line-height: 1.35; padding-right: 34px; margin-bottom: 20px; }
  .reason::after { content: ""; position: absolute; right: 0; top: 8px; width: 14px; height: 14px; border-radius: 50%; background: var(--white); }

  .cta { position: absolute; left: 520px; top: 1030px; width: 360px; height: 70px; background: var(--ink); display: flex; align-items: center; padding: 0 16px; gap: 14px; color: var(--white); }
  .cta-label { font-family: "Oswald", Arial, sans-serif; font-weight: 500; text-transform: uppercase; font-size: 17px; line-height: 1.05; border: 2px solid var(--white); padding: 4px 8px; }
  .cta-phone { font-family: "Oswald", Arial, sans-serif; font-weight: 700; font-size: 34px; letter-spacing: 1px; }

  .footer { position: absolute; left: 0; bottom: 0; width: 900px; height: 80px; background: var(--ink); display: flex; align-items: center; padding: 0 40px; }
  .footer-badge { width: 46px; height: 46px; border-radius: 50%; background: var(--grey); }
  .footer-web { flex: 1; text-align: center; color: var(--white); font-size: 24px; letter-spacing: 3px; padding-left: 160px; }
</style>
</head>
<body>
<main class="flyer">
  <svg class="shapes" width="900" height="1200" viewBox="0 0 900 1200">
    <defs>
      <linearGradient id="roofPhoto" x1="0" y1="0" x2="0" y2="1">
        <stop offset="0" stop-color="#9cc8ef"/>
        <stop offset="0.35" stop-color="#cfd8df"/>
        <stop offset="0.55" stop-color="#3a5f95"/>
        <stop offset="1" stop-color="#1f3b68"/>
      </linearGradient>
    </defs>
    <path d="M420 0 H900 V585 C760 640 620 600 520 640 C460 665 420 700 380 700 Z" fill="#141414"/>
    <path role="img" aria-label="Photo of an installer fitting solar panels on a house roof" d="M430 0 H900 V560 C760 610 620 575 520 615 C470 635 440 650 420 640 Z" fill="url(#roofPhoto)"/>
    <path d="M380 700 C430 690 470 650 530 640 C630 620 760 640 900 585 V1120 H380 C360 1000 350 800 380 700 Z" fill="#f47b20"/>
  </svg>

  <div class="brand">
    <span class="brand-mark"></span>
    <span class="brand-name">Tarnbrook<br>Services</span>
  </div>

  <h1 class="headline">
    What<br>will your<br><span class="dark">Electricity bill</span><br>look like<br><span class="last">in 5 years time?</span>
  </h1>

  <div class="portrait portrait-switchboard" role="img" aria-label="Photo of an electrician working at a switchboard"></div>
  <div class="portrait portrait-van" role="img" aria-label="Photo of an installer standing beside the company van"></div>

  <section class="reasons">
    <h2 class="reasons-title"><span class="big">3 Reasons to</span><span class="sub">Install Solar Pannel</span></h2>
    <ul class="reason-list">
      <li class="reason">The sun provides free, clean energy and is the best way to save money</li>
      <li class="reason">The government provides generous incentives saving you thousands of $$</li>
      <li class="reason">Advancing technology means you can store your energy and use it a night.</li>
    </ul>
  </section>

  <div class="cta">
    <span class="cta-label">Call for<br>free quote</span>
    <span class="cta-phone">0482 917 605</span>
  </div>

  <footer class="footer">
    <span class="footer-badge"></span>
    <span class="footer-web">www.tarnbrookservices.com.au</span>
  </footer>
</main>
</body>
</html>
```